Business Card Design Project

I want a design for my business cards based on an excisting logo design.

Target Market(s)

Marketeers, PR-peeps, CEO's, decisionmakers, entrepreneurs

Industry/Entity Type

Business

Requirements
Nice to have
• Some visual interest on the back too
Should not have
• Sarif on the font

```html
<!DOCTYPE html>
<html lang="nl">
<head>
<meta charset="utf-8">
<title>LeafLine PR – visitekaartjes</title>
<link rel="stylesheet" href="https://fonts.googleapis.com/css2?family=Questrial&display=swap">
<style>
  :root {
    --backdrop: #bac6c6;
    --card: #ffffff;
    --lime: #99ff00;
    --lime-soft: #c4fb6c;
    --ink: #111111;
    --brand-grey: #6b6b6b;
    --fine-grey: #8a8a8a;
  }
  * { margin: 0; padding: 0; box-sizing: border-box; }
  html, body { width: 1200px; height: 1000px; overflow: hidden; }
  body {
    background: var(--backdrop);
    font-family: "Questrial", "Century Gothic", sans-serif;
    color: var(--ink);
    position: relative;
  }
  .card {
    position: absolute;
    background: var(--card);
    overflow: hidden;
  }

  /* Front */
  .card-front { left: 51px; top: 282px; width: 519px; height: 336px; }
  .front-mark {
    position: absolute; left: 162px; top: 30px;
    width: 190px; height: 190px; border-radius: 50%;
    background: var(--lime);
  }
  .front-name {
    position: absolute; left: 0; right: 0; top: 226px;
    text-align: center; font-size: 31px; letter-spacing: 1px;
    color: var(--brand-grey);
  }
  .front-band {
    position: absolute; left: 0; right: 0; bottom: 0; height: 46px;
    background: var(--lime);
    display: flex; align-items: center; justify-content: center;
    font-size: 13.5px; color: var(--ink);
  }

  /* Back */
  .card-back { left: 632px; top: 282px; width: 514px; height: 332px; }
  .back-arc { position: absolute; left: 0; top: 0; }
  .contact-main {
    position: absolute; right: 30px; top: 40px;
    text-align: right; line-height: 27px;
  }
  .contact-name { font-size: 21px; }
  .contact-line { font-size: 19px; }
  .contact-details {
    position: absolute; left: 29px; top: 180px;
    font-size: 13.5px; line-height: 19.5px;
  }
  .back-brand {
    position: absolute; left: 27px; top: 275px;
    display: flex; align-items: center;
  }
  .back-mark {
    width: 27px; height: 27px; border-radius: 50%;
    background: var(--lime);
    margin-right: 9px;
  }
  .back-name { font-size: 19px; color: var(--brand-grey); letter-spacing: .5px; }
  .back-tagline {
    position: absolute; left: 213px; top: 286px;
    font-size: 9px; color: var(--fine-grey);
  }
</style>
</head>
<body>
  <section class="card card-front">
    <div class="front-mark"></div>
    <div class="front-name">LeafLine PR</div>
    <div class="front-band">Systemisch en strategisch PR-, marketing- en communicatieadvies</div>
  </section>

  <section class="card card-back">
    <svg class="back-arc" width="514" height="332" viewBox="0 0 514 332" aria-hidden="true">
      <path d="M228 0 A228 171 0 0 1 0 171 L0 93 A108 93 0 0 0 108 0 Z" fill="var(--lime-soft)"/>
    </svg>
    <div class="contact-main">
      <div class="contact-name">Marlies Vonk</div>
      <div class="contact-line">+31(0)6 20481937</div>
      <div class="contact-line">marlies.vonk@leaflinepr.nl</div>
    </div>
    <div class="contact-details">
      <div>Adress: Lindelaan 12 6711 AB Ede</div>
      <div>Web: leaflinepr.nl</div>
      <div>Chirper: chirper.com/_leaflinepr</div>
      <div>Pagebook: pagebook.com/leaflinepr</div>
    </div>
    <div class="back-brand">
      <div class="back-mark"></div>
      <div class="back-name">LeafLine PR</div>
    </div>
    <div class="back-tagline">Systemisch en strategisch PR-, marketing- en communicatieadvies</div>
  </section>
</body>
</html>
```